Why engage Insight Harborworks?

We are starting a new company that will perform usability consulting and offer usability lab rental. We are in need a one page description flyer.
Updates

Wow! We saw some very interesting and creative flyers posted for review in our contest.

Unfortunately, my schedule became a bit crazy and I may not get back to evaluating them until next week :(  In the meantime, I did want to say thank you for your entries!

Cheers!
Merle

Target Market(s)

product designers, human factors/usability researchers, consumer researcher firms, etc

Industry/Entity Type

It Company

Requirements
Must have
• We would like to see designs with a simple, yet modern, sophisticated feel. I will include our logo images that need to be incorporated along with the font used.

The file called flyer.pdf has all of the information that needs to be included.

Please include 1-3 appropriate stock photos. Please see text in flyer.pdf for description of our services.

Nice to have
• Additionally, there is a sample flyer design that we like for reference. Not a requirement...it is just a reference for the kind of style that we are looking for.

```html
<!DOCTYPE html>
<html lang="en">
<head>
<meta charset="utf-8">
<title>Insight Harborworks – Flyer</title>
<link rel="stylesheet" href="https://fonts.googleapis.com/css2?family=Source+Sans+3:wght@400;600;700&display=swap">
<style>
  :root {
    --navy: #1f3566;
    --navy-deep: #17294f;
    --green: #8cc43f;
    --green-text: #6f9e2c;
    --panel: #e3edcf;
    --rule: #9aa88a;
    --ink: #1b1b1b;
    --white: #ffffff;
    --font: "Source Sans 3", "Myriad Pro", Arial, sans-serif;
  }
  * { box-sizing: border-box; margin: 0; padding: 0; }
  html, body { width: 927px; height: 1200px; overflow: hidden; background: var(--white); }
  body { font-family: var(--font); color: var(--ink); }
  .flyer { position: relative; width: 927px; height: 1200px; overflow: hidden; background: var(--white); }

  .photo-lab {
    position: absolute; left: 0; top: 0; width: 456px; height: 350px;
    background: linear-gradient(180deg, #3b3f46 0%, #6d6a62 35%, #8a5a48 60%, #2f5a2a 100%);
  }
  .photo-team {
    position: absolute; left: 462px; top: 0; width: 465px; height: 174px;
    background: linear-gradient(120deg, #1d4c8a 0%, #5f8fc4 45%, #d9dee6 100%);
  }
  .brand {
    position: absolute; left: 462px; top: 174px; width: 465px; height: 176px;
    background: var(--white); padding: 42px 0 0 40px;
  }
  .brand-name {
    display: flex; align-items: center; gap: 14px;
    font-weight: 600; color: var(--navy); font-size: 44px; line-height: 0.95; letter-spacing: 0.5px;
    text-transform: uppercase;
  }
  .brand-dot { width: 34px; height: 34px; border-radius: 50%; background: var(--green); flex: none; }
  .brand-address { margin-top: 14px; font-weight: 700; font-size: 16px; color: var(--navy); }

  .intro-band {
    position: absolute; left: 0; top: 350px; width: 927px; height: 180px; background: var(--navy);
  }
  .intro {
    position: absolute; top: 362px; color: var(--white); font-size: 15px; line-height: 1.3;
  }
  .intro--left { left: 50px; width: 400px; }
  .intro--right { left: 474px; width: 410px; }

  .reasons {
    position: absolute; left: 48px; top: 498px; width: 840px; height: 632px;
    background: var(--panel); border-radius: 16px; overflow: hidden;
    display: flex;
  }
  .reasons-title {
    width: 60px; flex: none; background: var(--green); position: relative;
  }
  .reasons-title span {
    position: absolute; left: 50%; top: 50%;
    transform: translate(-50%, -50%) rotate(-90deg);
    white-space: nowrap; color: var(--white); font-weight: 600; font-size: 27px; letter-spacing: 1.5px;
    text-transform: uppercase;
  }
  .reasons-list { flex: 1; padding: 4px 14px 0 14px; }
  .reason {
    display: grid; grid-template-columns: 152px 1fr; column-gap: 8px;
    border-bottom: 1px solid var(--rule); padding-top: 8px;
  }
  .reason:last-child { border-bottom: none; }
  .reason-label { color: var(--green-text); font-size: 16px; font-weight: 600; line-height: 1.15; }
  .reason-text { font-size: 11.6px; line-height: 1.55; color: var(--ink); padding-top: 2px; }

  .footer {
    position: absolute; left: 0; top: 1143px; width: 927px; height: 57px; background: var(--navy);
    display: flex; align-items: center; color: var(--white); font-weight: 700; font-size: 25px; letter-spacing: 0.6px;
  }
  .footer-phone { display: flex; align-items: center; gap: 8px; margin-left: 66px; }
  .footer-web { margin-left: 70px; }
</style>
</head>
<body>
<div class="flyer">
  <div class="photo-lab" role="img" aria-label="Photo: researchers in lab coats looking down into a cutaway dollhouse with people in its rooms"></div>
  <div class="photo-team" role="img" aria-label="Photo: professionals working with laptops and a network of digital icons"></div>

  <div class="brand">
    <div class="brand-name"><span class="brand-dot"></span><span>Insight<br>Harborworks</span></div>
    <p class="brand-address">4120 N. Juniper Ridge Road, Tempe AZ 85281</p>
  </div>

  <div class="intro-band"></div>
  <p class="intro intro--left">We are a network of human factors engineers, usability specialists, and cognitive/consumer psychologists, who help you design and evaluate the usefulness, usability and desirability of your products.</p>
  <p class="intro intro--right">Lease our state of the art consumer research and usability lab, or partner with us on usability testing, eyetracking studies, participatory design, online survey research, ethnographic studies, focus groups and more.</p>

  <section class="reasons">
    <div class="reasons-title"><span>Why engage Insight Harborworks?</span></div>
    <div class="reasons-list">
      <div class="reason" style="height:83px"><h3 class="reason-label">Experience</h3><p class="reason-text">Founded by a Professor of Cognitive Psychology and Human Factors with over twenty years of experience, our group includes MS and PhD level consultants with experience working for and consulting with companies like Lumenfield, Corvant, Medaris, Quillon, Northgate Hospitals, Ashby and Rowe, Veltrix, and Starvale.</p></div>
      <div class="reason" style="height:71px"><h3 class="reason-label">Service</h3><p class="reason-text">Full range of consumer research and usability services, including ethnography, participatory design, questionnaires, user diaries, usability testing, usability evaluation, card sorting, psychometric scaling, focus groups and more.</p></div>
      <div class="reason" style="height:65px"><h3 class="reason-label">Range of products and industries</h3><p class="reason-text">Our consultants have extensive experience in design and evaluation of computing, web, tablet, smart phone, product, medical, consumer, and many other types of products and user interfaces.</p></div>
      <div class="reason" style="height:56px"><h3 class="reason-label">Client Service Specialist</h3><p class="reason-text">Need copies, printing, lunch, or dinner reservations? Our client service specialist will make sure you have everything you need.</p></div>
      <div class="reason" style="height:62px"><h3 class="reason-label">Recruiting</h3><p class="reason-text">Sizable database with ability to recruit research participants according to age, sex, occupation, health status, and other parameters.</p></div>
      <div class="reason" style="height:56px"><h3 class="reason-label">Onsite or remote streaming video</h3><p class="reason-text">Sessions can be viewed in many ways: Through our observation mirror, in our meeting room via pan-tilt-zoom camera, at your site on your computer, on your tablet or phone.</p></div>
      <div class="reason" style="height:33px"><h3 class="reason-label">Audio/video</h3><p class="reason-text">On-site video editing. Highlight video included in facility rental.</p></div>
      <div class="reason" style="height:38px"><h3 class="reason-label">Office space</h3><p class="reason-text">Meeting room for work, phone calls and conference calls. Wireless Internet.</p></div>
      <div class="reason" style="height:58px"><h3 class="reason-label">Accessibility</h3><p class="reason-text">Located on the first floor, with ample, free, convenient and handicap parking. Adjustable artificial and natural lighting.</p></div>
      <div class="reason" style="height:56px"><h3 class="reason-label">Transcription</h3><p class="reason-text">Transcription services and word frequency key-words-in-context, and word co-occurrence analyses available</p></div>
      <div class="reason" style="height:45px"><h3 class="reason-label">Bilingual</h3><p class="reason-text">Several consultants fluent in both English and Spanish</p></div>
    </div>
  </section>

  <footer class="footer">
    <span class="footer-phone">
      <svg width="22" height="26" viewBox="0 0 22 26" aria-hidden="true"><path d="M5 1 L9 1 L10 7 L7 9 C8 13 10 16 13 18 L15.5 15.5 L21 17 L21 21.5 C21 23.5 19 25 16.5 24.5 C8 23 2 15 1 6 C0.8 3 2.5 1 5 1 Z" fill="#ffffff"/></svg>
      480.555.0147
    </span>
    <span class="footer-web">WWW.INSIGHT-HARBORWORKS.COM</span>
  </footer>
</div>
</body>
</html>
```